Schulungen und Brandschutzdienstleistungen
Zielgruppe
Wir sind im vorbeugenden und organisatorischen Brandschutz tätig. Unsere Zielgruppe sind Firmen die Unterstützung, Beratung und die Schulung Ihrer Mitarbeiter beötigen.
Aufgabenstellung
Vorgaben ergeben sich aus dem Design der Homepage und dem pdf Upload (Beispiel des letzten Flyers).
Es sollen die Schulungsleistungen wie Brandschutzhelfer, Erste Hilfe und Unterweisungen hervorgehoben werden. Weiterhin sollen unsere Dienstleistungen, insbesondere der externe Brandschutzbeauftragte, aufgezeigt werden.
Schön währe auf der letzten Seite ein Anmeldeformular für die Schulungen.
Texte und Logo dürfen gerne verwendet werden.
Die Flyer soll zusammen mit einem Anschreiben in eine DIN lang Briefumschlag passen.

```html
<!DOCTYPE html>
<html lang="de">
<head>
<meta charset="utf-8">
<title>Brandschutz Kolbeck – Schulungen und Dienstleistungen</title>
<link href="https://fonts.googleapis.com/css2?family=Source+Sans+3:wght@400;600;700;800&display=swap" rel="stylesheet">
<style>
  :root {
    --red: #8c0f14;
    --red-text: #8e1a1c;
    --white: #ffffff;
    --ink: #1d1d1b;
    --line: #3a3a3a;
    --photo-warm: #c9b8a8;
    --photo-cool: #9aa1a8;
    --hall-light: #e4e6e6;
    --extinguisher: #d6231d;
  }
  * { box-sizing: border-box; margin: 0; padding: 0; }
  html, body { width: 1200px; height: 856px; overflow: hidden; background: var(--white); }
  body { font-family: "Source Sans 3", "Myriad Pro", Arial, sans-serif; color: var(--ink); }
  .flyer { position: relative; width: 1200px; height: 856px; overflow: hidden; background: var(--white); }

  /* left panel */
  .panel-left { position: absolute; left: 0; top: 0; width: 399px; height: 856px; }
  .panel-left .photo { position: absolute; left: 0; top: 0; width: 399px; height: 420px;
    background: linear-gradient(160deg, var(--photo-cool) 0%, var(--photo-warm) 45%, #7d7f86 100%); }
  .panel-left svg { position: absolute; left: 0; top: 0; }
  .course-title { position: absolute; left: 19px; top: 313px; font-size: 35px; font-weight: 700;
    color: var(--red-text); letter-spacing: .2px; white-space: nowrap; }
  .course-text { position: absolute; left: 27px; top: 410px; width: 360px; color: var(--white);
    font-size: 13.8px; line-height: 20.1px; }
  .course-text span { display: block; white-space: nowrap; text-align: justify; text-align-last: justify; }
  .course-text span.end { text-align-last: left; }
  .course-text span.gap { height: 20.1px; }

  /* middle panel */
  .panel-mid { position: absolute; left: 399px; top: 0; width: 389px; height: 856px; }
  .form-title { position: absolute; left: 23px; top: 16px; font-size: 32px; font-weight: 700; color: var(--red-text); white-space: nowrap; }
  .field { position: absolute; left: 23px; width: 351px; display: flex; align-items: flex-end; font-size: 15.5px; }
  .field span { white-space: nowrap; margin-right: 3px; }
  .field i { flex: 1; border-bottom: 1px solid var(--line); height: 1px; margin-bottom: 3px; }
  .choice-intro { position: absolute; left: 15px; top: 380px; font-size: 16.3px; color: var(--red-text); font-weight: 600; white-space: nowrap; }
  .choices { position: absolute; left: 15px; top: 410px; display: flex; gap: 24px; font-size: 16px; color: var(--red-text); font-weight: 600; }
  .choices label { display: flex; align-items: center; gap: 7px; white-space: nowrap; }
  .box { width: 19px; height: 19px; border: 1.5px solid var(--red-text); display: inline-block; }
  .date-pref { position: absolute; left: 23px; top: 466px; display: flex; align-items: flex-end;
    font-size: 16.3px; color: var(--red-text); font-weight: 600; white-space: nowrap; }
  .date-pref i { width: 141px; margin-left: 2px; border-bottom: 1px solid var(--line); margin-bottom: 3px; }
  .sign { position: absolute; top: 569px; text-align: center; font-size: 15.5px; border-top: 1px solid var(--line); padding-top: 3px; }
  .reach { position: absolute; left: 0; width: 389px; top: 661px; text-align: center; font-size: 21.5px; font-weight: 700; color: var(--red-text); }

  /* bottom band */
  .band { position: absolute; left: 399px; top: 704px; width: 801px; height: 152px; background: var(--red); }
  .contact { position: absolute; top: 717px; color: var(--white); text-align: center; font-size: 12.6px; line-height: 16.8px; font-style: normal; white-space: nowrap; }
  .contact strong { font-weight: 700; }

  /* right panel */
  .panel-right { position: absolute; left: 788px; top: 0; width: 412px; height: 788px; }
  .hero { position: absolute; left: 0; top: 151px; width: 412px; height: 637px;
    background: linear-gradient(180deg, var(--hall-light) 0%, #b9bcbd 40%, #c95a4f 70%, var(--extinguisher) 100%); }
  .brand-box { position: absolute; left: 0; top: 0; width: 412px; height: 151px; background: var(--red); }
  .brand-name { position: absolute; left: 14px; top: 12px; color: var(--white); font-size: 55px; font-weight: 700;
    line-height: 63px; letter-spacing: 1px; white-space: nowrap; }
  .ribbon { position: absolute; left: 28px; top: 512px; width: 400px; height: 96px; background: var(--red);
    transform: rotate(-8deg); transform-origin: left top; color: var(--white); font-weight: 700;
    font-size: 35px; line-height: 40px; text-align: center; padding: 8px 10px 0 0; letter-spacing: .5px; white-space: nowrap; }
  .year { position: absolute; left: 916px; top: 763px; color: var(--white); font-size: 70px; font-weight: 800; letter-spacing: 1px; }
</style>
</head>
<body>
<div class="flyer">

  <section class="panel-left">
    <div class="photo" role="img" aria-label="Foto: Teilnehmer üben Herzdruckmassage an einer Übungspuppe im Erste-Hilfe-Kurs"></div>
    <svg width="399" height="856" viewBox="0 0 399 856" aria-hidden="true">
      <polygon points="0,308 399,308 399,363 0,400" fill="#ffffff" fill-opacity="0.72"/>
      <polygon points="0,408 399,363 399,856 0,856" fill="var(--red)"/>
    </svg>
    <h2 class="course-title">ERSTE-HILFE-KURSE:</h2>
    <div class="course-text">
      <span>At que ventis serspientia estia dollis rem volore rehen-</span>
      <span>di con endigen dellibustrum aruntia spiendent dollam</span>
      <span>fugitis mintinus ea adigendelis destis dolorro quatur</span>
      <span>solorrunt eum num inulpa pla nuscilibus, susci netus</span>
      <span>rest, odipsa con nobis corum nimintcis est, unt velenis</span>
      <span>voluptati occum dolor aut est porumquae porepellite</span>
      <span class="gap"></span>
      <span>est, occus, que postia pore etur si reperchilit unt aliati</span>
      <span>nobisimus, omnim imini atur senimol uptati ullandel</span>
      <span>est, idi del ium volor aute voluptas et ius diae incipsum</span>
      <span>fugiaep erspersped quiatur accabore ommolorendam</span>
      <span>ernam, il est acea ditatia nus aria conserum quo quis</span>
      <span>cum et volo od quidia sit incius porro consedi quaes-</span>
      <span>trum soluptia quid elenisquid quas qui dolo officabo.</span>
      <span class="end">Itatur?</span>
      <span class="gap"></span>
      <span>At lant as et, idusandi cullit, conserum velicia sequi</span>
      <span class="end">aborro ipicidi ne suntem haria ime nimpore pernat.</span>
      <span class="end">To doluptatus explam nus.</span>
      <span>Tem es moluptasime esequid eraepro vidusda ndebis</span>
      <span>aspici odias sum quiaes alitatur magnihiliqui to iur?</span>
    </div>
  </section>

  <section class="panel-mid">
    <h2 class="form-title">ANMELDEFORMULAR:</h2>
    <div class="field" style="top:72px"><span>Name:</span><i></i></div>
    <div class="field" style="top:118px"><span>Vorname:</span><i></i></div>
    <div class="field" style="top:167px"><span>Straße:</span><i></i></div>
    <div class="field" style="top:216px"><span>PLZ, Wohnort:</span><i></i></div>
    <div class="field" style="top:267px"><span>Telefon:</span><i></i></div>
    <div class="field" style="top:315px"><span>E-Mail:</span><i></i></div>
    <p class="choice-intro">Ich möchte an folgender Schulung teilnehmen:</p>
    <div class="choices">
      <label><span class="box"></span>Brandschutzhelfer</label>
      <label><span class="box"></span>Erste Hilfe</label>
    </div>
    <div class="date-pref"><span>Als Termin bevorzuge ich den:</span><i></i></div>
    <div class="sign" style="left:23px;width:130px">Datum</div>
    <div class="sign" style="left:194px;width:180px">Unterschrift</div>
    <h3 class="reach">So erreichen Sie uns:</h3>
  </section>

  <section class="panel-right">
    <div class="hero" role="img" aria-label="Foto: roter Feuerlöscher vor einem Brandschutzschild in einem hellen Flur"></div>
    <div class="brand-box"></div>
    <h1 class="brand-name">BRANDSCHUTZ<br>KOLBECK</h1>
    <div class="ribbon">SCHULUNGEN UND<br>DIENSTLEISTUNGEN</div>
  </section>

  <div class="band"></div>
  <address class="contact" style="left:399px;width:182px">
    <strong>Brandschutz Kolbeck</strong><br>
    Lindenhofstrasse 12<br>
    36118 Birkenau<br><br>
    (06681) 5501234<br>
    info@brandschutz-kolbeck.de
  </address>
  <div class="contact" style="left:602px;width:190px">
    Besuchen Sie uns im Web:<br><br>
    <strong>www.brandschutz-kolbeck.de</strong><br><br>
    Seminare und Schulungen<br>auch online buchbar.
  </div>
  <div class="year">2017</div>

</div>
</body>
</html>
```